Packaging designed for both the bar and the box for retail and online sales

The name of the product is Plume Crumb. We manufacture a consumer package good product that's a healthy edible cookie dough bar. The product look, feels and tastes like cookie dough. It's sold in the refrigerator section of retail stores next to cookie dough and tundra loaf. The product is Gluten Free, Diary Free and include B-12, Biotin and Collagen. The ingredients are natural. When design this think about who eat cookie dough and how to engage the buyer in purchasing the product.

We needs design packaging designed for both the bar and the box. I have attached the die lines for both products.

Target Market(s)

Our customer is 16-45. Primarily female but really anyone. Middle to upper income. Interest include healthy life style and yoga. Like to eat something sweet but not feel guilty.

Colors

Designer to choose colors to be used in the design.

Requirements
Must have
• Must be clean, warm, inviting. Brand designs I really like are Tundra Loaf.
Should not have
• Should not have a photo of food

```html
<!DOCTYPE html>
<html lang="en">
<head>
<meta charset="utf-8">
<title>Plume Crumb – Bar Wrapper</title>
<link rel="stylesheet" href="https://fonts.googleapis.com/css2?family=Oswald:wght@400&family=Open+Sans:wght@400&display=swap">
<style>
  :root {
    --plum: #8c5187;
    --plum-dark: #6f4f76;
    --plum-stripe: #7e4679;
    --gold: #d2a150;
    --gold-deep: #c08a3a;
    --gold-soft: #e9c98e;
    --gold-pale: #f3e2c0;
    --crumb-light: #e3bb72;
    --foil: #f4f4f5;
    --foil-shade: #d9d9dc;
    --icon: #c9bccb;
    --page: #ffffff;
  }
  * { box-sizing: border-box; margin: 0; padding: 0; }
  html, body {
    width: 1078px; height: 1200px; overflow: hidden;
    background: var(--page);
  }
  .canvas { position: relative; width: 1078px; height: 1200px; }
  .wrapper {
    position: absolute; top: 108px; width: 326px; height: 962px;
    display: flex; flex-direction: column;
  }
  .wrapper--plain { left: 113px; }
  .wrapper--filled { left: 622px; }

  .crimp {
    height: 96px; position: relative;
    background: repeating-linear-gradient(90deg, var(--plum) 0 3px, var(--plum-stripe) 3px 5px);
  }
  .crimp svg { position: absolute; left: 0; width: 326px; height: 12px; display: block; }
  .crimp--top svg { top: 0; }
  .crimp--bottom svg { bottom: 0; }

  .seal-band {
    height: 53px;
    background: linear-gradient(180deg, var(--plum-dark) 0%, var(--plum) 40%);
  }
  .claim {
    height: 42px; background: var(--gold);
    display: flex; align-items: center; justify-content: center;
    font-family: 'Oswald', sans-serif; font-weight: 400;
    font-size: 21px; letter-spacing: -0.2px; color: #fff;
  }
  .front {
    height: 569px; position: relative;
    background: linear-gradient(90deg, var(--foil-shade) 0%, var(--foil) 8%, #fff 50%, var(--foil) 92%, var(--foil-shade) 100%);
  }
  .art {
    position: absolute; border-radius: 28px;
  }
  .wrapper--plain .art {
    left: 27px; top: 60px; width: 272px; height: 260px;
    background: linear-gradient(160deg, var(--gold-pale) 0%, var(--gold-soft) 100%);
    border: 3px solid var(--gold);
  }
  .wrapper--filled .art {
    left: 26px; top: 44px; width: 278px; height: 296px;
    background: linear-gradient(160deg, var(--crumb-light) 0%, var(--gold) 55%, var(--gold-deep) 100%);
  }
  .brand-name {
    position: absolute; left: 0; right: 0; top: 352px;
    text-align: center;
    font-family: 'Oswald', sans-serif; font-weight: 400;
    font-size: 78px; line-height: 1.02; color: var(--plum);
  }
  .base {
    height: 106px; position: relative;
    background: var(--plum-dark);
    display: flex; align-items: flex-start; padding: 20px 0 0 12px;
  }
  .badge {
    width: 86px; display: flex; flex-direction: column; align-items: center;
    font-family: 'Open Sans', sans-serif; font-size: 12.5px; color: var(--icon);
  }
  .badge svg { width: 60px; height: 60px; margin-bottom: 2px; color: var(--icon); }
  .weight {
    position: absolute; right: 34px; top: 34px;
    font-family: 'Oswald', sans-serif; font-size: 24px; color: var(--icon);
  }
</style>
</head>
<body>
<main class="canvas">
  <svg width="0" height="0" style="position:absolute" aria-hidden="true">
    <defs>
      <pattern id="teeth-up" width="18.11" height="12" patternUnits="userSpaceOnUse">
        <polygon points="0,0 9,12 18.11,0" fill="#fff"/>
      </pattern>
      <pattern id="teeth-down" width="18.11" height="12" patternUnits="userSpaceOnUse">
        <polygon points="0,12 9,0 18.11,12" fill="#fff"/>
      </pattern>
      <g id="gluten-free">
        <circle cx="30" cy="30" r="27" fill="none" stroke="currentColor" stroke-width="2"/>
        <line x1="30" y1="12" x2="30" y2="50" stroke="currentColor" stroke-width="2"/>
        <ellipse cx="25" cy="22" rx="4" ry="6" fill="none" stroke="currentColor" stroke-width="1.6"/>
        <ellipse cx="35" cy="22" rx="4" ry="6" fill="none" stroke="currentColor" stroke-width="1.6"/>
        <ellipse cx="25" cy="33" rx="4" ry="6" fill="none" stroke="currentColor" stroke-width="1.6"/>
        <ellipse cx="35" cy="33" rx="4" ry="6" fill="none" stroke="currentColor" stroke-width="1.6"/>
        <line x1="11" y1="11" x2="49" y2="49" stroke="currentColor" stroke-width="2"/>
      </g>
      <g id="dairy-free">
        <circle cx="30" cy="30" r="27" fill="none" stroke="currentColor" stroke-width="2"/>
        <path d="M26 12 h8 v5 l4 7 v24 h-16 v-24 l4 -7 z" fill="none" stroke="currentColor" stroke-width="1.8"/>
        <line x1="22" y1="30" x2="38" y2="30" stroke="currentColor" stroke-width="1.6"/>
        <line x1="11" y1="11" x2="49" y2="49" stroke="currentColor" stroke-width="2"/>
      </g>
    </defs>
  </svg>

  <section class="wrapper wrapper--plain">
    <div class="crimp crimp--top"><svg viewBox="0 0 326 12"><rect width="326" height="12" fill="url(#teeth-up)"/></svg></div>
    <div class="seal-band"></div>
    <div class="claim">Include B12, Biotin and Collagen</div>
    <div class="front">
      <div class="art" role="img" aria-label="Gold outline illustration of a hot air balloon among three clouds"></div>
      <p class="brand-name">Plume<br>Crumb</p>
    </div>
    <div class="base">
      <div class="badge"><svg viewBox="0 0 60 60"><use href="#gluten-free"/></svg>Gluten Free</div>
      <div class="badge"><svg viewBox="0 0 60 60"><use href="#dairy-free"/></svg>Dairy Free</div>
      <span class="weight">60 g.</span>
    </div>
    <div class="crimp crimp--bottom"><svg viewBox="0 0 326 12"><rect width="326" height="12" fill="url(#teeth-down)"/></svg></div>
  </section>

  <section class="wrapper wrapper--filled">
    <div class="crimp crimp--top"><svg viewBox="0 0 326 12"><rect width="326" height="12" fill="url(#teeth-up)"/></svg></div>
    <div class="seal-band"></div>
    <div class="claim">Include B12, Biotin and Collagen</div>
    <div class="front">
      <div class="art" role="img" aria-label="Hot air balloon and clouds filled with a golden cookie dough texture"></div>
      <p class="brand-name">Plume<br>Crumb</p>
    </div>
    <div class="base">
      <div class="badge"><svg viewBox="0 0 60 60"><use href="#gluten-free"/></svg>Gluten Free</div>
      <div class="badge"><svg viewBox="0 0 60 60"><use href="#dairy-free"/></svg>Dairy Free</div>
      <span class="weight">60 g.</span>
    </div>
    <div class="crimp crimp--bottom"><svg viewBox="0 0 326 12"><rect width="326" height="12" fill="url(#teeth-down)"/></svg></div>
  </section>
</main>
</body>
</html>
```